Tourism Marketing needing sleek, clear design for business card & proposal documents.

***Company background***
"Quiet Harbour" is a company specializing in tourism marketing and project management. We do international wholesale, event management as well as ongoing representation of tourism and hospitality companies.

***Target market***
We cater to tourism companies and hotel professionals.

***Task***
We would like to get a single sided business card designed (but will still consider two sided, we are open to any ideas you may have). The layout for this card should be modern and elegant. Currently we do not have a logo, but we would like our business name in a really simple typography for the business card (similar to Moonrise Palace's logo - www.moonrisepalace-example.com.au).We are after a design that is clear, strong enough to be recognised as Quiet Harbour that does not require any fancy design. Another option is a simple play on QH (Quiet Harbour) or simply have Quiet Harbour featured elsewhere on card more as a brand/logo.

Feel free to submit different fonts if you feel you have any other fonts/designs that may be suitable for this card other than sans serifs. Should this project be successful, we will be considering several other projects for business proposal templates and eventually a website design.

The information that needs to go on the card are as follows:

Marta Holloway
Director
Quiet Harbour
Tourism Marketing & Representation
87 Wendover Parade
Lindenvale, Queensland, 4217 Australia
T +61 498203617 E marta@quietharbour-example.com.au

***Look and feel***
We'd like the business card design to express the following:
Modern, sleek, elegant, simple, discreet, quality, subtle, professional, creative, innovation

In terms of typography, we like something really simple and blocky (similar font to Moonrise Palace's logo - www.moonrisepalace-example.com.au)

***Colour scheme***
Shades of grey and dark teal

***Note***
Although our main target market are professionals, we would like the business card design to be versatile enough to be used outside of the tourism industry and need to appeal to different markets.

I do not have existing logo. Was hoping for a design that may be clear, strong enough not to require one. Other option is a simple play on QH (Quiet Harbour) or simply have Quiet Harbour featured elsewhere on card more as a brand/logo.

Marta Holloway
Director
Quiet Harbour Pty Ltd 
87 Wendover Parade
T +61 498203617  E  marta@quietharbour-example.com.au

Thank you for designs so far. Many have used a mauve colour which matches our company profile. This is not necessary, as that is just a draft and will be completely redesigned, so dont  feel you need to incorporate the mauve.

My colour preferences are for a white or grey background, and I like fonts in dark teals, grey or other sophisticated but modern colours. feel free to submit different fonts if you you have other fonts you thing would be suitable for this card, along with sans serifs. Should this project be successful, we will be considering several others for business proposal templates and eventually website. 

Target Market(s)

International Hospitality Senior Executives, Directors of International Tourism Companies, Directors of Tourism Bodies Internationally, local Tourism

Industry/Entity Type

Hospitality

Requirements
Should not have
• must not have bright garish colour, swirly patterns or anything that dates too much.

```html
<!DOCTYPE html>
<html lang="en">
<head>
<meta charset="utf-8">
<title>Quiet Harbour – Business Card</title>
<link rel="stylesheet" href="https://fonts.googleapis.com/css2?family=Montserrat:wght@300;400;600;700&display=swap">
<style>
  :root {
    --ink-black: #000000;
    --harbour-navy: #00233a;
    --mark-blue: #023b5e;
    --rule-grey: #8c8c8c;
    --title-grey: #7d7d7d;
    --text-grey: #8a8a8a;
    --address-grey: #6f7a82;
  }
  html, body {
    margin: 0;
    padding: 0;
    width: 1200px;
    height: 685px;
    overflow: hidden;
    background: var(--ink-black);
  }
  .card {
    position: relative;
    width: 1200px;
    height: 685px;
    background: var(--ink-black);
    font-family: "Montserrat", sans-serif;
    overflow: hidden;
  }
  .card > * { position: absolute; margin: 0; line-height: 1; white-space: nowrap; }

  .brand-square {
    left: 87px; top: 83px;
    width: 204px; height: 204px;
    background: var(--mark-blue);
  }
  .brand-name {
    left: 322px; top: 127px;
    font-size: 64px; font-weight: 600;
    letter-spacing: 0.1em;
    color: var(--title-grey);
  }
  .brand-tagline {
    left: 323px; top: 208px;
    font-size: 26px; font-weight: 400;
    letter-spacing: 0.24em;
    color: var(--title-grey);
  }

  .name-frame {
    left: 541px; top: 297px;
    width: 700px; height: 140px;
    border-top: 2px solid var(--rule-grey);
    border-left: 2px solid var(--rule-grey);
    box-sizing: border-box;
  }
  .person-name {
    left: 569px; top: 318px;
    font-size: 42px; font-weight: 300;
    letter-spacing: 0.06em;
    color: var(--text-grey);
  }
  .person-role {
    left: 569px; top: 375px;
    font-size: 33px; font-weight: 700;
    letter-spacing: 0.09em;
    color: var(--text-grey);
  }

  .contact-band {
    left: 0; top: 436px;
    width: 1200px; height: 249px;
    background: var(--harbour-navy);
    border-top: 2px solid var(--rule-grey);
    box-sizing: border-box;
  }
  .contact-line {
    left: 127px;
    font-size: 26px; font-weight: 400;
    letter-spacing: 0.2em;
    color: var(--address-grey);
  }
  .contact-street { top: 499px; }
  .contact-city { top: 548px; }
  .contact-reach { top: 594px; letter-spacing: 0.1em; }
</style>
</head>
<body>
  <div class="card">
    <div class="brand-square" aria-hidden="true"></div>
    <h1 class="brand-name">QUIET HARBOUR</h1>
    <p class="brand-tagline">TOURISM MARKETING &amp; REPRESENTATION</p>

    <div class="contact-band" aria-hidden="true"></div>
    <div class="name-frame" aria-hidden="true"></div>
    <p class="person-name">Marta Holloway</p>
    <p class="person-role">DIRECTOR</p>

    <p class="contact-line contact-street">87 WENDOVER PARADE</p>
    <p class="contact-line contact-city">LINDENVALE, QUEENSLAND, 4217 AUSTRALIA</p>
    <p class="contact-line contact-reach">T +61 498203617 E MARTA@QUIETHARBOUR-EXAMPLE.COM.AU</p>
  </div>
</body>
</html>
```